social interest sharing site needs a web site design

we need a web site design for a social web platform.
the site is one page(main page), that is split into 3 sections
each section is a different color(red,green and blue)
and a user can choose to share each of the sections.
any section/color will contain boxes , each box can contain different media types.

the media types:
* list of URLS
* list of articles including title + image + description
* list of videos
* thumbnails of images
* calender
* list of emails

the main content will look like corkboardly layout
multiple boxes each box can contain different type of content as described above

each color is a different tab
each tab will have layout like corkboardly
Updates

please read the last description update.
and i uploaded an image that can explain the requirements better

thanks
Oren
 

Industry/Entity Type

Media

```html
<!DOCTYPE html>
<html lang="en">
<head>
<meta charset="utf-8">
<title>Pinwell.me – Home</title>
<link rel="stylesheet" href="https://fonts.googleapis.com/css2?family=Source+Sans+3:wght@400;600;700&family=Arimo:wght@400;700&display=swap">
<style>
:root{
  --red:#b5121b;
  --green:#0f9475;
  --blue:#0c4f96;
  --header:#1d1d1d;
  --social:#3a6aa6;
  --signup:#16997a;
  --tab-yellow:#f7b62a;
  --panel:#ffffff;
  --text:#2b2b2b;
  --muted:#6b6b6b;
  --link:#1a5fa6;
  --pink:#c2187a;
  --cal-arrow:#5e7f86;
  --cal-line:#dedede;
  --cal-today:#b9bb8e;
  --footer:#3e6fb0;
  --mail:#f2a93b;
  --go:#5b8ff0;
  --play:#2aa388;
}
*{box-sizing:border-box;margin:0;padding:0}
html,body{width:871px;height:1200px;overflow:hidden}
body{
  position:relative;
  font-family:"Source Sans 3",Arial,sans-serif;
  color:var(--text);
  background:
    linear-gradient(100deg,rgba(255,255,255,0) 30%,rgba(60,60,60,.45) 48%,rgba(255,255,255,0) 62%),
    linear-gradient(180deg,#8f8f8f 0%,#d9d9d9 25%,#9a9a9a 55%,#cfcfcf 80%,#7d7d7d 100%);
}
.top-bar{position:absolute;left:0;top:0;width:871px;height:96px;background:var(--header)}
.brand{position:absolute;left:0;top:0;width:248px;height:160px;display:flex}
.brand-tab{flex:1;color:#fff;font-size:11px;line-height:12px;padding:112px 16px 0 12px}
.brand-tab--red{background:var(--red)}
.brand-tab--green{background:var(--green)}
.brand-tab--blue{background:var(--blue)}
.brand-name{position:absolute;left:14px;top:52px;color:#fff;font-size:34px;font-weight:700;letter-spacing:-.5px}
.social{position:absolute;top:24px;left:426px;display:flex;gap:4px}
.social-btn{width:48px;height:48px;background:var(--social);border:1px solid #6f93c4;display:flex;align-items:center;justify-content:center}
.login{position:absolute;left:676px;top:38px;color:#fff;font-weight:700;font-size:17px}
.signup{position:absolute;left:727px;top:32px;width:99px;height:29px;background:var(--signup);color:#fff;font-weight:700;font-size:17px;text-align:center;line-height:28px;border-radius:2px}
.following{position:absolute;left:258px;top:111px;color:#fff;font-weight:700;font-size:13px;line-height:13px}
.shared-tab{position:absolute;top:108px;height:32px;background:var(--tab-yellow);color:#fff;font-size:10px;line-height:11px;padding:5px 12px;border-radius:2px;box-shadow:0 2px 3px rgba(0,0,0,.3)}
.settings{position:absolute;left:0;top:188px;width:34px;height:36px;background:#fff;display:flex;align-items:center;justify-content:center}
.panel{position:absolute;background:var(--panel);box-shadow:0 4px 10px rgba(0,0,0,.35)}
/* articles */
.articles{left:46px;top:192px;width:439px;height:343px;padding:14px 28px 0 26px}
.article{display:flex;gap:9px;padding:12px 0 14px;border-bottom:1px dashed #bbb}
.article-thumb{flex:0 0 68px;height:68px;border-radius:3px;background:linear-gradient(135deg,#163a5e,#4a8cbc)}
.article-title{font-family:"Arimo",Arial,sans-serif;font-weight:700;font-size:13px;margin:2px 0 6px}
.article-text{font-size:9.6px;line-height:13px}
.article-text a{color:var(--link);text-decoration:underline}
.view-all{display:inline-block;margin-top:12px;color:var(--pink);font-size:9.5px;text-decoration:underline}
/* videos */
.videos{left:508px;top:192px;width:316px;height:298px;padding:10px 21px}
.video-grid{display:grid;grid-template-columns:127px 127px;column-gap:20px;row-gap:4px}
.video-thumb{position:relative;height:98px;border:1px solid #999;box-shadow:0 1px 3px rgba(0,0,0,.3)}
.video-thumb--teal{background:linear-gradient(160deg,#3a93a3,#2a7f8e)}
.video-thumb--white{background:linear-gradient(160deg,#f7f7f7,#dcdcdc)}
.video-thumb--grey{background:linear-gradient(160deg,#eef1f4,#c9d3dc)}
.video-thumb--dark{background:linear-gradient(160deg,#163a44,#05090b)}
.video-play{position:absolute;left:50%;top:50%;width:30px;height:28px;margin:-14px 0 0 -15px;background:var(--play);display:flex;align-items:center;justify-content:center}
.video-caption{font-size:9.4px;line-height:13px;color:var(--muted);margin:7px 0 0 4px;height:30px}
.video-caption--link{text-decoration:underline}
/* urls */
.urls{left:46px;top:551px;width:439px;height:213px;padding:7px 30px 0 18px;overflow:hidden}
.url-list{list-style:none;font-size:9.4px;line-height:14.4px;color:#333;white-space:nowrap}
.url-list .active{color:var(--link);text-decoration:underline}
.scrollbar{position:absolute;right:6px;top:6px;width:10px;height:200px;border:1px solid #ccc;background:#f3f3f3}
.scrollbar span{position:absolute;left:1px;top:18px;width:6px;height:90px;background:#e1e1e1;border:1px solid #c9c9c9}
/* calendar */
.calendar{left:46px;top:793px;width:436px;height:335px}
.cal-head{height:53px;display:flex;align-items:center;justify-content:center;border-bottom:1px solid var(--cal-line);font-family:"Arimo",Arial,sans-serif;font-weight:700;font-size:18px;color:#555;letter-spacing:.5px}
.cal-arrow{position:absolute;top:0;width:29px;height:53px;background:var(--cal-arrow);display:flex;align-items:center;justify-content:center}
.cal-grid{position:absolute;left:28px;top:66px;display:grid;grid-template-columns:repeat(7,54px);font-family:"Arimo",Arial,sans-serif;color:#666;font-size:13px}
.cal-day{height:30px;text-align:center;font-weight:700;color:#555}
.cal-date{height:40px;border:1px solid var(--cal-line);margin:-1px 0 0 -1px;display:flex;align-items:center;justify-content:center}
.cal-date--muted{color:#c8c8c8}
.cal-date--today{background:var(--cal-today);color:#fff}
.cal-note{position:absolute;left:184px;top:187px;width:173px;height:59px;background:#fff;border:1px solid #ccc;box-shadow:0 2px 6px rgba(0,0,0,.3);padding:6px;font-size:9px}
.cal-note-input{color:#bbb;height:17px;margin-bottom:7px}
.cal-note-row{display:flex;justify-content:space-between;align-items:center;border-top:1px solid #ddd;padding-top:4px;color:#555}
.cal-go{background:var(--go);color:#fff;width:46px;height:19px;line-height:19px;text-align:center}
/* photos */
.photos{left:508px;top:503px;width:316px;height:389px;padding:13px 21px}
.photo-grid{display:grid;grid-template-columns:repeat(3,82px);column-gap:13px;row-gap:12px}
.photo{position:relative;height:82px;border:2px solid #333;border-radius:3px;overflow:hidden}
.photo--sky{background:linear-gradient(160deg,#4f96d2,#3c7fb8)}
.photo--field{background:linear-gradient(160deg,#5b9ccf,#5f9a45)}
.photo--warm{background:linear-gradient(160deg,#8a6d55,#5c4636)}
.photo--sea{background:linear-gradient(160deg,#4d7fa6,#2f6a80)}
.photo--dusk{background:linear-gradient(160deg,#3a4f70,#2c3448)}
.photo--night{background:linear-gradient(160deg,#1a3152,#35597e)}
.photo-credit{position:absolute;left:0;right:0;bottom:4px;text-align:center;color:#fff;font-size:6px;line-height:7px;font-weight:700}
.photo-credit em{display:block;font-weight:400}
/* mail */
.mail{left:508px;top:916px;width:316px;height:212px;padding:10px 10px 0 10px}
.mail-row{display:grid;grid-template-columns:24px 66px 1fr 26px;column-gap:4px;height:31.4px;font-size:9.4px;line-height:12px}
.mail-from,.mail-time{font-weight:700;color:#222;font-family:"Arimo",Arial,sans-serif;font-size:9px}
.mail-subject{color:var(--muted)}
.mail-subject b{color:#222;font-family:"Arimo",Arial,sans-serif}
/* footer */
.footer{position:absolute;left:0;top:1156px;width:871px;height:44px;background:var(--footer);color:#fff;font-size:11.5px;display:flex;align-items:center;padding-left:44px}
.footer-links{position:absolute;left:515px;top:18px}
.footer-colors{position:absolute;right:0;top:0;height:44px;display:flex}
.footer-colors span{width:38px}
</style>
</head>
<body>
<header>
  <div class="top-bar"></div>
  <nav class="brand">
    <a class="brand-tab brand-tab--red">My home</a>
    <a class="brand-tab brand-tab--green">My favorites videos</a>
    <a class="brand-tab brand-tab--blue">Personal apps</a>
    <span class="brand-name">Pinwell.me</span>
  </nav>
  <div class="social">
    <span class="social-btn" aria-label="Social network one"></span>
    <span class="social-btn" aria-label="Social network two"></span>
    <span class="social-btn" aria-label="Help"><svg width="26" height="32" viewBox="0 0 26 32"><path d="M5 10a8 8 0 1 1 12 6c-3 2-4 3-4 6" fill="none" stroke="#fff" stroke-width="5"/><rect x="10" y="25" width="6" height="6" fill="#fff"/></svg></span>
    <span class="social-btn" aria-label="Search"><svg width="30" height="30" viewBox="0 0 30 30"><circle cx="17" cy="12" r="8" fill="none" stroke="#fff" stroke-width="4"/><path d="M11 18 3 26" stroke="#fff" stroke-width="5" stroke-linecap="round"/></svg></span>
  </div>
  <a class="login">Login</a>
  <a class="signup">Sign up</a>
  <div class="following">Following<br>Pinwell</div>
  <a class="shared-tab" style="left:318px;width:110px">Talias favorites<br>videos</a>
  <a class="shared-tab" style="left:450px;width:108px">Mayas pics +<br>favorites links</a>
  <a class="shared-tab" style="left:577px;width:108px">Familiy weekly<br>calendar and notes</a>
</header>

<div class="settings" aria-label="Settings"><svg width="20" height="20" viewBox="0 0 20 20"><g fill="#111"><circle cx="10" cy="10" r="6"/><rect x="8" y="0" width="4" height="20"/><rect x="0" y="8" width="20" height="4"/><rect x="8" y="0" width="4" height="20" transform="rotate(45 10 10)"/><rect x="8" y="0" width="4" height="20" transform="rotate(-45 10 10)"/></g><circle cx="10" cy="10" r="2.5" fill="#fff"/></svg></div>

<main>
  <section class="panel articles">
    <article class="article">
      <div class="article-thumb" role="img" aria-label="Article image: hand touching a digital screen"></div>
      <div><h3 class="article-title">Lorem Ipsum. Proin gravida nibh vel velit auctor</h3>
      <p class="article-text">Lorem Ipsum. Proin gravida nibh vel velit auctor aliquet. Aenean sollicitudin, lorem quis bibendum auctor, nisi elit consequat ipsum, nec sagittis sem nibh id elit. Duis sed odio sit amet nibh......<a>Read more</a></p></div>
    </article>
    <article class="article">
      <div class="article-thumb" role="img" aria-label="Article image: hand touching a digital screen"></div>
      <div><h3 class="article-title">Lorem Ipsum. Proin gravida nibh vel velit auctor</h3>
      <p class="article-text">Lorem Ipsum. Proin gravida nibh vel velit auctor aliquet. Aenean sollicitudin, lorem quis bibendum auctor, nisi elit consequat ipsum, nec sagittis sem nibh id elit. Duis sed odio sit amet nibh......<a>Read more</a></p></div>
    </article>
    <article class="article">
      <div class="article-thumb" role="img" aria-label="Article image: hand touching a digital screen"></div>
      <div><h3 class="article-title">Lorem Ipsum. Proin gravida nibh vel velit auctor</h3>
      <p class="article-text">Lorem Ipsum. Proin gravida nibh vel velit auctor aliquet. Aenean sollicitudin, lorem quis bibendum auctor, nisi elit consequat ipsum, nec sagittis sem nibh id elit. Duis sed odio sit amet nibh......<a>Read more</a></p></div>
    </article>
    <a class="view-all">View All</a>
  </section>

  <section class="panel videos">
    <div class="video-grid">
      <div>
        <div class="video-thumb video-thumb--teal" role="img" aria-label="Video still: fruit illustration"><span class="video-play"><svg width="12" height="14"><path d="M0 0 12 7 0 14z" fill="#fff"/></svg></span></div>
        <p class="video-caption video-caption--link">Lorem Ipsum. Proin gravida nibh vel velit auctor</p>
      </div>
      <div>
        <div class="video-thumb video-thumb--white" role="img" aria-label="Video still: phone with growth chart"><span class="video-play"><svg width="12" height="14"><path d="M0 0 12 7 0 14z" fill="#fff"/></svg></span></div>
        <p class="video-caption">Lorem Ipsum. Proin gravida nibh vel velit auctor</p>
      </div>
      <div>
        <div class="video-thumb video-thumb--grey" role="img" aria-label="Video still: globe with app icons"><span class="video-play"><svg width="12" height="14"><path d="M0 0 12 7 0 14z" fill="#fff"/></svg></span></div>
        <p class="video-caption">Lorem Ipsum. Proin gravida nibh vel velit auctor</p>
      </div>
      <div>
        <div class="video-thumb video-thumb--dark" role="img" aria-label="Video still: futuristic motorbike at night"><span class="video-play"><svg width="12" height="14"><path d="M0 0 12 7 0 14z" fill="#fff"/></svg></span></div>
        <p class="video-caption">Lorem Ipsum. Proin gravida nibh vel velit auctor</p>
      </div>
    </div>
  </section>

  <section class="panel urls">
    <ul class="url-list">
      <li>http://www.corkboardly.com/search/pins/?q=videos</li>
      <li>file:///C:/Users/Dana/Desktop/pinwell%20copy.jpg</li>
      <li>http://blog.harborcorner.com/2013/12/premium-wordpress-themes-responsive-retina-ready/</li>
      <li>http://www.corkboardly.com/pin/410531322254219328/</li>
      <li>http://www.corkboardly.com/</li>
      <li class="active">http://jobs.craftcrowd.com/job.aspx?id=340052&amp;src=rec</li>
      <li>http://sketchhub.com/web-design/contests/create-homep</li>
      <li>age-brand-high-end-artisan-perfume-china-273917/brief</li>
      <li>http://sketchhub.com/web-design/contests/create-homep</li>
      <li>age-brand-high-end-artisan-perfume-china-273917/entries</li>
      <li>http://www.craftcrowd.com/myprofile.aspx</li>
      <li>http://www.craftcrowd.com/contact.aspxhttp://sketch-</li>
      <li>hub.com/web-design/contests/create-homepage-brand-high-end-artisan-perfume-crief</li>
      <li>http://sketchhub.com/web-design/contests/create-homepage-brand-high-end-artisan-pe</li>
    </ul>
    <div class="scrollbar"><span></span></div>
  </section>

  <section class="panel calendar">
    <span class="cal-arrow" style="left:0"><svg width="12" height="18"><path d="M10 2 3 9l7 7" fill="none" stroke="#fff" stroke-width="3"/></svg></span>
    <div class="cal-head">NOVEMBER</div>
    <span class="cal-arrow" style="right:0"><svg width="12" height="18"><path d="M2 2l7 7-7 7" fill="none" stroke="#fff" stroke-width="3"/></svg></span>
    <div class="cal-grid">
      <div class="cal-day">Mon</div><div class="cal-day">Tue</div><div class="cal-day">Wed</div><div class="cal-day">Thu</div><div class="cal-day">Fri</div><div class="cal-day">Sat</div><div class="cal-day">Sun</div>
      <div class="cal-date">1</div><div class="cal-date">2</div><div class="cal-date">3</div><div class="cal-date">4</div><div class="cal-date">5</div><div class="cal-date">6</div><div class="cal-date">7</div>
      <div class="cal-date">8</div><div class="cal-date">9</div><div class="cal-date">10</div><div class="cal-date">11</div><div class="cal-date">12</div><div class="cal-date">13</div><div class="cal-date">14</div>
      <div class="cal-date">15</div><div class="cal-date">16</div><div class="cal-date">17</div><div class="cal-date">18</div><div class="cal-date">19</div><div class="cal-date">20</div><div class="cal-date">21</div>
      <div class="cal-date">22</div><div class="cal-date">23</div><div class="cal-date">24</div><div class="cal-date">25</div><div class="cal-date">26</div><div class="cal-date">27</div><div class="cal-date">28</div>
      <div class="cal-date">29</div><div class="cal-date cal-date--today">30</div><div class="cal-date">31</div><div class="cal-date cal-date--muted">1</div><div class="cal-date cal-date--muted">2</div><div class="cal-date cal-date--muted">3</div><div class="cal-date cal-date--muted">4</div>
    </div>
    <div class="cal-note">
      <div class="cal-note-input">I still need to do ...</div>
      <div class="cal-note-row"><span>17 November 2013</span><span class="cal-go">Go</span></div>
    </div>
  </section>

  <section class="panel photos">
    <div class="photo-grid">
      <div class="photo photo--field" role="img" aria-label="Photo: meadow with river"><p class="photo-credit">LENA KORAT<em>* UI/UX Designer *</em></p></div>
      <div class="photo photo--sky" role="img" aria-label="Photo: sprout under blue sky"><p class="photo-credit">LENA KORAT<em>* UI/UX Designer *</em></p></div>
      <div class="photo photo--warm" role="img" aria-label="Portrait photo"><p class="photo-credit">LENA KORAT<em>* UI/UX Designer *</em></p></div>
      <div class="photo photo--field" role="img" aria-label="Photo: sky over a field"><p class="photo-credit">LENA KORAT<em>* UI/UX Designer *</em></p></div>
      <div class="photo photo--sky" role="img" aria-label="Photo: flowers and butterfly"><p class="photo-credit">LENA KORAT<em>* UI/UX Designer *</em></p></div>
      <div class="photo photo--field" role="img" aria-label="Photo: flowers under blue sky"><p class="photo-credit">LENA KORAT<em>* UI/UX Designer *</em></p></div>
      <div class="photo photo--sea" role="img" aria-label="Photo: coastal cliffs"><p class="photo-credit">LENA KORAT<em>* UI/UX Designer *</em></p></div>
      <div class="photo photo--sea" role="img" aria-label="Photo: rock arch at sea"><p class="photo-credit">LENA KORAT<em>* UI/UX Designer *</em></p></div>
      <div class="photo photo--sky" role="img" aria-label="Photo: lake with mountains"><p class="photo-credit">LENA KORAT<em>* UI/UX Designer *</em></p></div>
      <div class="photo photo--sea" role="img" aria-label="Photo: lake at sunset"><p class="photo-credit">LENA KORAT<em>* UI/UX Designer *</em></p></div>
      <div class="photo photo--night" role="img" aria-label="Photo: night sky over ice"><p class="photo-credit">LENA KORAT<em>* UI/UX Designer *</em></p></div>
      <div class="photo photo--dusk" role="img" aria-label="Photo: hillside town at dusk"><p class="photo-credit">LENA KORAT<em>* UI/UX Designer *</em></p></div>
    </div>
  </section>

  <section class="panel mail">
    <div class="mail-row"><svg width="22" height="16" viewBox="0 0 22 16"><rect width="22" height="16" rx="1" fill="var(--mail)"/><path d="M1 1l10 8 10-8" fill="none" stroke="#fff" stroke-width="1.5"/></svg><span class="mail-from">Lorem Ipsum</span><span class="mail-subject"><b>Lorem Ipsum. Proin</b> gravida nibh vel velit auctor</span><span class="mail-time">5:02</span></div>
    <div class="mail-row"><svg width="22" height="16" viewBox="0 0 22 16"><rect width="22" height="16" rx="1" fill="var(--mail)"/><path d="M1 1l10 8 10-8" fill="none" stroke="#fff" stroke-width="1.5"/></svg><span class="mail-from">Lorem Ipsum</span><span class="mail-subject"><b>Lorem Ipsum. Proin</b> gravida nibh vel velit auctor amet lorem</span><span class="mail-time">5:02</span></div>
    <div class="mail-row"><svg width="22" height="16" viewBox="0 0 22 16"><rect width="22" height="16" rx="1" fill="var(--mail)"/><path d="M1 1l10 8 10-8" fill="none" stroke="#fff" stroke-width="1.5"/></svg><span class="mail-from">Lorem Ipsum</span><span class="mail-subject"><b>Lorem Ipsum. Proin</b> gravida nibh vel velit auctor</span><span class="mail-time">5:02</span></div>
    <div class="mail-row"><svg width="22" height="16" viewBox="0 0 22 16"><rect width="22" height="16" rx="1" fill="var(--mail)"/><path d="M1 1l10 8 10-8" fill="none" stroke="#fff" stroke-width="1.5"/></svg><span class="mail-from">Lorem Ipsum</span><span class="mail-subject"><b>Lorem Ipsum. Proin</b> gravida nibh vel velit auctor amet lorem</span><span class="mail-time">5:02</span></div>
    <div class="mail-row"><svg width="22" height="16" viewBox="0 0 22 16"><rect width="22" height="16" rx="1" fill="var(--mail)"/><path d="M1 1l10 8 10-8" fill="none" stroke="#fff" stroke-width="1.5"/></svg><span class="mail-from">Lorem Ipsum</span><span class="mail-subject"><b>Lorem Ipsum. Proin</b> gravida nibh vel velit auctor</span><span class="mail-time">5:02</span></div>
    <div class="mail-row"><svg width="22" height="16" viewBox="0 0 22 16"><rect width="22" height="16" rx="1" fill="var(--mail)"/><path d="M1 1l10 8 10-8" fill="none" stroke="#fff" stroke-width="1.5"/></svg><span class="mail-from">Lorem Ipsum</span><span class="mail-subject"><b>Lorem Ipsum. Proin</b> gravida nibh vel velit auctor amet lorem</span><span class="mail-time">5:02</span></div>
  </section>
</main>

<footer class="footer">
  <span>Copyright © 2013 Pinwell.me. All Rights Reserved.</span>
  <span class="footer-links">About Us &nbsp;|&nbsp; Advertise &nbsp;|&nbsp; Write For Us &nbsp;|&nbsp; Contact Us</span>
  <div class="footer-colors"><span style="background:var(--red)"></span><span style="background:var(--green)"></span><span style="background:var(--blue)"></span></div>
</footer>
</body>
</html>
```